International Clinical Software Company needs a new business card design

We are looking for a new business card design for our company that has recently expanded into the UK market, making us a multinational company.
After having rebranded our website and produced a new style guide, we are looking for a business card that is creative and attention grabbing, while being consistent with the style and colour scheme used on the new website, www.brookvale.example
We produce care management technology for the aged care market, but the main aspect we aim to communicate is the human element of our software, and the way it assists in providing better care for aged people, and stronger relationships between aged people and the staff that care for them.
Our current business card is a dark green with gold text, which makes the text quite difficult to read, not very aesthetically appealing and the colour scheme looks quite dated.
We would like something fresh and modern, that can still be colourful but doesn't use large blocks of dark colour, and uses the colours within our logo.
Something tying in with the leaves that are used in our logo could work quite nicely, along with the Autumn/Fall colours of soft greens, yellows and reds (also in our existing logo). However also happy to look at fresh, completely out of the box ideas we may not have yet considered.
Target Market(s)
The people that receive this business card work in the aged card or health industry and are either corporate/management level staff or clinical (Registered Nurses, care workers etc.)
Industry/Entity Type
Health Product
Contact Information for Business Card
Company Name - BrookvaleTech
Company locations: United Kingdom, Australia, New Zealand
Staff Details:
Staff name: Dermot Quill
Staff job title: Executive Chairman
Staff email: d.quill@brookvale.example
Office phone number: 01632 960418
Font styles to use
Other font styles liked:
- Calibri
Requirements
Must have
- Must include the BrookvaleTech brand name in it's current font
- Must include logo (3 leaves in gold circle)
- Must include Business Card Details
Nice to have
- Elements of gold
- White space
- Something autumn themed but not too cliched
Should not have
- No blue - used by a major competitor and we would like to differentiate from them
- Large blocks of dark green colour (the green that appears in our leaves on the logo on our current business card is the background colour and it is far too dark)

```html
<!DOCTYPE html>
<html lang="en">
<head>
<meta charset="utf-8">
<title>BrookvaleTech — Business Card</title>
<link rel="stylesheet" href="https://fonts.googleapis.com/css2?family=Carlito:wght@400;700&display=swap">
<style>
  :root {
    --page-bg: #ece8e1;
    --leaf-green: #5c9c3c;
    --leaf-green-deep: #4b8a30;
    --autumn-red: #b81a40;
    --gold: #dcd64a;
    --logo-sand: #d8c9a0;
    --ink-white: #ffffff;
  }
  * { box-sizing: border-box; margin: 0; padding: 0; }
  html, body {
    width: 1200px;
    height: 1022px;
    overflow: hidden;
    background: var(--page-bg);
    font-family: "Carlito", "Calibri", sans-serif;
  }
  .business-card {
    position: absolute;
    left: 100px;
    top: 225px;
    width: 1000px;
    height: 572px;
    border-radius: 22px;
    overflow: hidden;
    background: linear-gradient(160deg, var(--leaf-green) 0%, var(--leaf-green-deep) 100%);
    box-shadow: 0 10px 30px rgba(0,0,0,0.18);
    color: var(--ink-white);
  }
  .card-artwork {
    position: absolute;
    inset: 0;
    width: 100%;
    height: 100%;
  }
  .brand {
    position: absolute;
    left: 70px;
    top: 200px;
    display: flex;
    align-items: center;
    gap: 26px;
  }
  .brand-circle {
    width: 150px;
    height: 150px;
    border-radius: 50%;
    background: var(--logo-sand);
    border: 4px solid var(--ink-white);
  }
  .brand-name {
    font-size: 68px;
    font-weight: 400;
    color: var(--ink-white);
    letter-spacing: 1px;
  }
  .contact {
    position: absolute;
    right: 44px;
    top: 52px;
    text-align: right;
  }
  .contact-name {
    font-size: 34px;
    font-weight: 700;
    text-transform: uppercase;
    letter-spacing: 0.5px;
  }
  .contact-title {
    font-size: 23px;
    color: var(--gold);
    margin-top: 2px;
  }
  .contact-line {
    display: flex;
    justify-content: flex-end;
    align-items: center;
    gap: 12px;
    font-size: 22px;
    margin-top: 18px;
  }
  .contact-line + .contact-line { margin-top: 10px; }
  .contact-icon { width: 20px; height: 20px; flex: none; }
  .locations {
    position: absolute;
    left: 510px;
    bottom: 34px;
    font-size: 26px;
    color: var(--ink-white);
    white-space: nowrap;
  }
</style>
</head>
<body>
  <section class="business-card" aria-label="BrookvaleTech business card">
    <svg class="card-artwork" viewBox="0 0 1000 572" preserveAspectRatio="none" aria-hidden="true">
      <path class="red-wave" d="M250 572 C 380 566, 500 470, 620 380 S 880 255 1000 250 L1000 572 Z" fill="var(--autumn-red)"/>
      <path class="gold-rule" d="M250 572 C 380 566, 500 470, 620 380 S 880 255 1000 250" fill="none" stroke="var(--gold)" stroke-width="5"/>
      <rect class="red-tab" x="896" y="0" width="64" height="30" fill="var(--autumn-red)"/>
    </svg>

    <div class="brand">
      <div class="brand-circle"></div>
      <div class="brand-name">BrookvaleTech</div>
    </div>

    <div class="contact">
      <div class="contact-name">Dermot Quill</div>
      <div class="contact-title">Executive Chairman</div>
      <div class="contact-line">
        <span>01632 960418</span>
        <svg class="contact-icon" viewBox="0 0 20 20" aria-hidden="true">
          <path d="M5 2 L8 6 L6.5 8 C7.5 10.5 9.5 12.5 12 13.5 L14 12 L18 15 L16 18 C9 17.5 2.5 11 2 4 Z" fill="var(--gold)"/>
        </svg>
      </div>
      <div class="contact-line">
        <span>d.quill@brookvale.example</span>
        <svg class="contact-icon" viewBox="0 0 20 20" aria-hidden="true">
          <rect x="2" y="4" width="16" height="12" fill="none" stroke="var(--gold)" stroke-width="2"/>
          <path d="M2 4 L10 11 L18 4" fill="none" stroke="var(--gold)" stroke-width="2"/>
        </svg>
      </div>
    </div>

    <div class="locations">United Kingdom Australia, New Zealand</div>
  </section>
</body>
</html>
```